Game Design from Mock ups

Looking for a simple design based on the images attached.

Should be a simple color scheme, not the same colored posted in the images. Flat design would be best.

Both pages should be designed (Menu and Gameplay)

```html
<!DOCTYPE html>
<html lang="en">
<head>
<meta charset="utf-8">
<title>Emoji Puzzles – Menu and Gameplay Screens</title>
<link rel="stylesheet" href="https://fonts.googleapis.com/css2?family=Source+Sans+3:wght@700;800&display=swap">
<style>
  :root {
    --page: #ffffff;
    --frame: #16302e;
    --screen: #1f6f6b;
    --accent: #f4a259;
    --on-accent: #16302e;
    --light: #ffffff;
    --key: #10302e;
  }
  html, body {
    margin: 0;
    padding: 0;
    width: 1200px;
    height: 938px;
    overflow: hidden;
    background: var(--page);
  }
  .screens {
    display: block;
    width: 1200px;
    height: 938px;
    font-family: "Source Sans 3", "Myriad Pro", sans-serif;
  }
  .device-frame { fill: var(--frame); }
  .screen-fill { fill: var(--screen); }
  .accent { fill: var(--accent); }
  .light { fill: var(--light); }
  .key { fill: var(--key); }
  .label { fill: var(--light); font-weight: 700; font-size: 35px; }
  .accent-label { fill: var(--on-accent); font-weight: 700; font-size: 35px; text-anchor: middle; }
  .title { fill: var(--light); font-weight: 700; font-size: 58px; text-anchor: middle; }
  .button-label { fill: var(--on-accent); font-weight: 700; font-size: 38px; text-anchor: middle; }
  .timer-label { fill: var(--light); font-weight: 700; font-size: 34px; }
  .key-letter { fill: var(--light); font-weight: 700; font-size: 31px; text-anchor: middle; }
  .round-number { fill: var(--light); font-weight: 700; font-size: 32px; text-anchor: middle; }
</style>
</head>
<body>
<svg class="screens" viewBox="0 0 1200 938" xmlns="http://www.w3.org/2000/svg">

  <!-- Menu screen -->
  <g class="menu-screen">
    <rect class="device-frame" x="155" y="168" width="412" height="601"/>
    <rect class="screen-fill" x="170" y="181" width="382" height="576"/>

    <text class="title" x="357" y="249">Emoji Puzzles</text>

    <text class="label" x="194" y="325">Join Game</text>
    <rect class="accent" x="409" y="294" width="116" height="39" rx="14"/>
    <text class="accent-label" x="467" y="326">Create</text>

    <rect class="accent" x="190" y="360" width="31" height="38" rx="10"/>
    <g class="lobby-list">
      <text class="label" x="232" y="392">3 Players</text><text class="label" x="423" y="392">Join&gt;</text>
      <text class="label" x="232" y="441">3 Players</text><text class="label" x="423" y="441">Join&gt;</text>
      <text class="label" x="232" y="488">3 Players</text><text class="label" x="423" y="488">Join&gt;</text>
      <text class="label" x="232" y="537">3 Players</text><text class="label" x="423" y="537">Join&gt;</text>
    </g>

    <rect class="accent" x="249" y="600" width="224" height="79" rx="12"/>
    <text class="button-label" x="361" y="653">PLAY GAME</text>
  </g>

  <!-- Gameplay screen -->
  <g class="game-screen">
    <rect class="device-frame" x="645" y="167" width="410" height="601"/>
    <rect class="screen-fill" x="659" y="180" width="384" height="576"/>

    <text class="timer-label" x="682" y="222">60”</text>
    <rect class="light" x="755" y="195" width="260" height="32" rx="16"/>
    <path class="accent" d="M771 195 H941 V227 H771 A16 16 0 0 1 771 195 Z"/>

    <g class="round-track">
      <rect class="light" x="673" y="236" width="56" height="35" rx="9"/>
      <rect class="light" x="733" y="236" width="56" height="35" rx="9"/>
      <rect class="light" x="792" y="236" width="56" height="35" rx="9"/>
      <rect class="light" x="851" y="236" width="56" height="35" rx="9"/>
      <rect class="light" x="911" y="236" width="56" height="35" rx="9"/>
      <rect class="key" x="970" y="236" width="56" height="35" rx="9"/>
      <text class="round-number" x="998" y="265">1</text>
    </g>

    <rect class="light clue-board" x="672" y="279" width="354" height="201" rx="12"/>

    <g class="answer-slots">
      <rect class="light" x="760" y="510" width="35" height="40" rx="10"/>
      <rect class="light" x="797" y="510" width="35" height="40" rx="10"/>
      <rect class="light" x="834" y="510" width="35" height="40" rx="10"/>
      <rect class="light" x="871" y="510" width="35" height="40" rx="10"/>
      <rect class="light" x="908" y="510" width="35" height="40" rx="10"/>
      <rect class="light" x="778" y="560" width="35" height="40" rx="10"/>
      <rect class="light" x="815" y="560" width="35" height="40" rx="10"/>
      <rect class="light" x="852" y="560" width="35" height="40" rx="10"/>
      <rect class="light" x="890" y="560" width="35" height="40" rx="10"/>
    </g>

    <g class="letter-keys">
      <g>
        <rect class="key" x="666" y="621" width="34" height="38" rx="15"/><text class="key-letter" x="683" y="651">Q</text>
        <rect class="key" x="703" y="621" width="34" height="38" rx="15"/><text class="key-letter" x="720" y="651">R</text>
        <rect class="key" x="741" y="621" width="34" height="38" rx="15"/><text class="key-letter" x="758" y="651">G</text>
        <rect class="key" x="778" y="621" width="34" height="38" rx="15"/><text class="key-letter" x="795" y="651">N</text>
        <rect class="key" x="815" y="621" width="34" height="38" rx="15"/><text class="key-letter" x="832" y="651">N</text>
        <rect class="key" x="851" y="621" width="34" height="38" rx="15"/><text class="key-letter" x="868" y="651">A</text>
        <rect class="key" x="888" y="621" width="34" height="38" rx="15"/><text class="key-letter" x="905" y="651">P</text>
        <rect class="key" x="926" y="621" width="34" height="38" rx="15"/><text class="key-letter" x="943" y="651">L</text>
        <rect class="key" x="963" y="621" width="34" height="38" rx="15"/><text class="key-letter" x="980" y="651">T</text>
        <rect class="key" x="1001" y="621" width="34" height="38" rx="15"/><text class="key-letter" x="1018" y="651">Z</text>
      </g>
      <g>
        <rect class="key" x="666" y="670" width="34" height="38" rx="15"/><text class="key-letter" x="683" y="700">Y</text>
        <rect class="key" x="703" y="670" width="34" height="38" rx="15"/><text class="key-letter" x="720" y="700">T</text>
        <rect class="key" x="741" y="670" width="34" height="38" rx="15"/><text class="key-letter" x="758" y="700">N</text>
        <rect class="key" x="778" y="670" width="34" height="38" rx="15"/><text class="key-letter" x="795" y="700">Q</text>
        <rect class="key" x="815" y="670" width="34" height="38" rx="15"/><text class="key-letter" x="832" y="700">U</text>
        <rect class="key" x="851" y="670" width="34" height="38" rx="15"/><text class="key-letter" x="868" y="700">N</text>
        <rect class="key" x="888" y="670" width="34" height="38" rx="15"/><text class="key-letter" x="905" y="700">W</text>
        <rect class="key" x="926" y="670" width="34" height="38" rx="15"/><text class="key-letter" x="943" y="700">S</text>
        <rect class="key" x="963" y="670" width="34" height="38" rx="15"/><text class="key-letter" x="980" y="700">X</text>
        <rect class="key" x="1001" y="670" width="34" height="38" rx="15"/><text class="key-letter" x="1018" y="700">N</text>
      </g>
    </g>
  </g>
</svg>
</body>
</html>
```